Business Card - Rebranding for Consulting Firm

We are renaming and rebranding our consulting firm and need to raise the level of quality of our cards as part of that effort. We consult to leading high tech, life science and other innovation sector companies.

Need a two-sided business card design.

Side 1: (a) Company logo (b) tag line: Get More From Every Hire You Make (c) Name (d) Title (e) Phone 1: Office (f) Phone 2: Mobile (g) email: person@HollowmereAdvisory.com

Side 2: Two lines of text: (a) Markets Shift Fast. Teams Must Adapt. People Deliver the Plan. (b) We guide you through each step.

Target Market(s)

Business and human resources executives and senior managers

Industry/Entity Type

Management Consulting

Contact Information for Business Card

Font styles to use
Sans Serif

Requirements
Must have
• clean, not too busy, but with a bit of creativity. Stick to the colors used in the attached logo
• appeal to high tech, life science companies
Nice to have
• prefer white background

```html
<!DOCTYPE html>
<html lang="en">
<head>
<meta charset="utf-8">
<title>Hollowmere Advisory – Business Card</title>
<link href="https://fonts.googleapis.com/css2?family=Didact+Gothic&family=Open+Sans:ital,wght@1,600&display=swap" rel="stylesheet">
<style>
  :root {
    --brand-blue: #0b5f9c;
    --text-gray: #8a8f94;
    --paper: #f7f7f6;
    --backdrop: #e4e6e8;
    --white: #ffffff;
  }
  * { margin: 0; padding: 0; box-sizing: border-box; }
  html, body { width: 1200px; height: 900px; overflow: hidden; }
  body {
    background: var(--backdrop);
    font-family: "Didact Gothic", "Century Gothic", sans-serif;
    position: relative;
  }
  .card {
    position: absolute;
    left: 300px;
    width: 600px;
    height: 343px;
    box-shadow: 0 6px 18px rgba(0,0,0,0.18);
    overflow: hidden;
  }
  .card--front { top: 90px; background: var(--paper); }
  .card--back { top: 467px; background: var(--brand-blue); color: var(--white); }

  .edge-tab { position: absolute; width: 8px; height: 30px; }
  .card--front .edge-tab { right: 0; top: 34px; background: var(--brand-blue); }
  .card--back .edge-tab { left: 0; bottom: 34px; background: var(--white); }

  .wordmark { position: absolute; line-height: 1; white-space: nowrap; }
  .wordmark__name { display: block; font-size: 44px; letter-spacing: -1px; }
  .wordmark__sub {
    display: block; font-family: "Didact Gothic", sans-serif;
    font-size: 10px; letter-spacing: 9px; margin-top: 4px; padding-left: 4px;
  }

  .card--front .wordmark { left: 56px; top: 52px; color: var(--brand-blue); }
  .card--back .wordmark { right: 78px; top: 118px; color: var(--white); }

  .tagline {
    position: absolute; left: 60px; top: 124px;
    color: var(--text-gray); font-size: 16px; white-space: nowrap;
  }

  .person { position: absolute; right: 50px; top: 150px; text-align: right; }
  .person__name { color: var(--brand-blue); font-size: 24px; }
  .person__title { color: var(--text-gray); font-size: 15px; }

  .contacts { position: absolute; left: 82px; top: 190px; }
  .contact { margin-bottom: 6px; line-height: 1.1; }
  .contact__label { display: block; color: var(--brand-blue); font-size: 14px; }
  .contact__value { display: block; color: var(--text-gray); font-size: 14px; padding-left: 10px; }

  .motto {
    position: absolute; left: 42px; bottom: 40px;
    font-family: "Open Sans", sans-serif; font-style: italic; font-weight: 600;
    font-size: 14px; line-height: 1.5; white-space: nowrap;
  }
  .motto__second { padding-left: 18px; }
</style>
</head>
<body>
  <section class="card card--front" aria-label="Business card front">
    <span class="edge-tab"></span>
    <div class="wordmark">
      <span class="wordmark__name">Hollowmere</span>
      <span class="wordmark__sub">ADVISORY LLC</span>
    </div>
    <p class="tagline">Get More From Every Hire You Make</p>
    <div class="person">
      <p class="person__name">Daniel Whitford</p>
      <p class="person__title">Director</p>
    </div>
    <div class="contacts">
      <p class="contact"><span class="contact__label">Mobile</span><span class="contact__value">+1 555 014-2612</span></p>
      <p class="contact"><span class="contact__label">Office</span><span class="contact__value">+1 555 014-2613</span></p>
      <p class="contact"><span class="contact__label">E-mail</span><span class="contact__value">person@HollowmereAdvisory.com</span></p>
    </div>
  </section>

  <section class="card card--back" aria-label="Business card back">
    <span class="edge-tab"></span>
    <div class="wordmark">
      <span class="wordmark__name">Hollowmere</span>
      <span class="wordmark__sub">ADVISORY LLC</span>
    </div>
    <div class="motto">
      <p>Markets Shift Fast. Teams Must Adapt. People Deliver the Plan.</p>
      <p class="motto__second">We guide you through each step.</p>
    </div>
  </section>
</body>
</html>
```